Business Card Design

Electronic Security Installation Specialists

Check out our website at www.bramblecoastllc.com to see what we do.

Industry/Entity Type

Business

Contact Information for Business Card

Fern Ridge
Marisol Penton
318 Calloway Drive
Calderwick, WV 26418

Colors
3176b5
0455a3
ffffff

```html
<!DOCTYPE html>
<html lang="en">
<head>
<meta charset="utf-8">
<title>Fern Ridge — Business Card</title>
<link rel="stylesheet" href="https://fonts.googleapis.com/css2?family=Archivo:wght@300;400;700&display=swap">
<style>
  :root {
    --brand-blue: #223c80;
    --band-blue: #1f3a7d;
    --paper: #ffffff;
    --ink: #111111;
    --rule: #555555;
    --metal-light: #e9eaec;
    --metal-mid: #c9cbcf;
    --metal-dark: #a7a9ad;
    --stage: #000000;
  }
  * { margin: 0; padding: 0; box-sizing: border-box; }
  html, body {
    width: 1200px; height: 1000px; overflow: hidden;
    background: var(--stage);
    font-family: "Archivo", "Helvetica Neue", Arial, sans-serif;
  }
  .canvas { position: relative; width: 1200px; height: 1000px; }

  .card { position: absolute; top: 369px; width: 446px; height: 246px; overflow: hidden; }

  /* Front */
  .card--front {
    left: 128px;
    background: linear-gradient(180deg, var(--metal-light) 0%, var(--metal-mid) 55%, var(--metal-dark) 100%);
  }
  .brand-mark { position: absolute; left: 31px; top: 24px; }
  .brand-name {
    position: absolute; left: 245px; top: 74px;
    color: var(--brand-blue);
    font-weight: 400;
    font-size: 52px; line-height: 54px;
    letter-spacing: -0.5px;
    text-transform: uppercase;
  }

  /* Back */
  .card--back { left: 626px; background: var(--paper); }
  .holder-name {
    position: absolute; left: 21px; top: 52px;
    color: var(--brand-blue);
    font-size: 28px; line-height: 29px;
    text-transform: uppercase;
  }
  .holder-name .given { font-weight: 300; display: block; }
  .holder-name .family { font-weight: 700; display: block; }
  .address {
    position: absolute; left: 21px; top: 121px;
    color: var(--ink);
    font-size: 18px; line-height: 23px; font-weight: 400;
    font-style: normal;
  }
  .write-lines { position: absolute; left: 222px; top: 57px; width: 203px; }
  .write-lines span {
    display: block; height: 1px; background: var(--rule); margin-bottom: 41px;
  }
  .tagline-band {
    position: absolute; left: 0; top: 200px; width: 100%; height: 25px;
    background: var(--band-blue);
    color: var(--paper);
    font-size: 14.5px; line-height: 25px; font-weight: 400; letter-spacing: 0.6px;
    text-align: center; text-transform: uppercase;
  }
</style>
</head>
<body>
<main class="canvas">
  <section class="card card--front" aria-label="Card front">
    <svg class="brand-mark" width="196" height="196" viewBox="0 0 196 196" aria-hidden="true">
      <circle cx="98" cy="98" r="96" fill="var(--brand-blue)"/>
    </svg>
    <h1 class="brand-name">Fern<br>Ridge</h1>
  </section>

  <section class="card card--back" aria-label="Card back">
    <h2 class="holder-name">
      <span class="given">Marisol</span>
      <span class="family">Penton</span>
    </h2>
    <address class="address">
      318 Calloway Drive<br>
      Calderwick<br>
      WV 26418
    </address>
    <div class="write-lines" aria-hidden="true">
      <span></span><span></span><span></span><span></span>
    </div>
    <p class="tagline-band">Electronic Security Installation Specialists</p>
  </section>
</main>
</body>
</html>
```